Vermilion Reel Works Web Design

COMPANY: VERMILION REEL WORKS
LOCATION: SHANGHAI, CHINA
AREA: FILM/TV DRAMA/COMMERCIALS/GAME POST PRODUCTION, SOUND DESIGN, MUSIC, and GAME.
WEB STYLE: SIMPLE, PROFESSIONAL, TRUSTWORTHY

LANGUAGE: ENGLISH, CHINESE. (Same layout, different language)
UPDATE: AFTER PROJECT FINISHED, WE NEED UPDATE BY OURSELVES.

MAIN SUBJECT: 6
1 HOMEPAGE
2 ABOUT US
3 TEAM
4 SERVICES
5 FACILITY
6 CONTACT

add one page of JOB OPPORTUNITIES.

DETAILS
1 HOMEPAGE
SLOGAN: Vermilion Reel Works provides a well-designed working environment which amplifies your team’s ability to reach their creative goals.

Our services include:
 Feature Films
 Music & Scoring
 Commercials
 ADR & Foley
 Sound & Picture Editorial
 Sound Design
 Video Game

2 ABOUT US
Vermilion Reel Works is located in the premiere South-Bund area of Shanghai. Occupying a 5000 square meter Technical Building, Vermilion Reel Works was built by a filmmaker for filmmakers, and is one of the largest, most versatile full-service post-production facilities in China.

Vermilion Reel Works is positioning to be at the forefront of the latest technology. Our goal is to provide a comprehensive solution for the post-production needs of our clients. We offer two fully-equipped dubbing stages (one of which will be certified KESTRON VOXAR PREMIERE), a large variety of both picture and sound editing rooms, impressive Foley and ADR stages, a world-class scoring stage, and complete audio and video transfer services.

We can handle your entire project from editing all the way to the end of the final sound mix; all under one extremely comfortable roof. We fully realize that the true art is in listening to the needs of our clients and making their greatest vision a reality. To this end our creative team's expertise, with a network of sound supervisors, editors and mixers, will deliver the magic you need. Producers and directors will also find our richly appointed guest accommodations to be a comfortable and soothing place to wind up the day. Every aspect of your project will be taken care of by a skilled and dedicated team, in the way that is best suited to you.

3 TEAM
(attachment 01)

4 SERVICES
Sound Mix
ADR
FOLEY
MUSIC
Sound Design
Sound Edit
Picture Edit
for all the Films, TV Drama, Commercials, Video Games, Online Media
(attachment 02, use photo)

5 FACILITY
(attachment 03)

6 CONTACT
(attachment04)
with map

Project Deadline Extended
Reason: Designers work are great, my bosses will spend 1-2 days select one of these web design, and spend 1-2 days to make some change, maybe use new photos.

```html
<!DOCTYPE html>
<html lang="en">
<head>
<meta charset="utf-8">
<title>Vermilion Reel Works</title>
<link rel="stylesheet" href="https://fonts.googleapis.com/css2?family=Arimo:wght@400;700&family=Roboto+Condensed:wght@700&display=swap">
<style>
  :root {
    --ink: #000000;
    --white: #ffffff;
    --gold: #f7c400;
    --active: #1aa33a;
    --shade-deep: #121414;
    --shade-mid: #2b2f2c;
    --glow-teal: #3d6b5e;
    --glow-amber: #5a4a1c;
    --magenta: #c8137f;
    --violet: #5b2a9a;
    --blue: #1a7fd0;
    --teal: #14a39a;
    --green: #2fae3a;
    --lime: #b5d51a;
    --yellow: #f5e20a;
    --orange: #f08a0c;
    --red: #e5163a;
    --arrow-bg: rgba(90, 90, 90, 0.75);
  }
  * { margin: 0; padding: 0; box-sizing: border-box; }
  html, body { width: 1200px; height: 686px; overflow: hidden; background: var(--ink); }
  .site { position: relative; width: 1200px; height: 686px; overflow: hidden; font-family: "Arimo", Arial, sans-serif; }

  .masthead { position: absolute; top: 0; left: 0; width: 1200px; height: 88px; background: var(--ink); z-index: 3; }
  .brand { position: absolute; left: 90px; top: 27px; font-weight: 700; font-size: 26.5px; line-height: 30px; color: var(--gold); white-space: nowrap; }

  .main-nav { position: absolute; top: 0; left: 0; width: 1200px; height: 88px; }
  .main-nav a { position: absolute; top: 40px; color: var(--white); text-decoration: none; font-size: 12px; line-height: 14px; white-space: nowrap; }
  .main-nav .is-active::before { content: ""; position: absolute; top: -40px; left: -5px; right: -3px; height: 6px; background: var(--active); }
  .nav-home { left: 618px; }
  .nav-about { left: 682px; }
  .nav-team { left: 773px; }
  .nav-services { left: 831px; }
  .nav-facility { left: 910px; }
  .nav-contact { left: 985px; }
  .nav-career { left: 1062px; }

  .spectrum-rule { position: absolute; top: 86px; left: 0; width: 1200px; height: 3px; z-index: 3;
    background: linear-gradient(90deg, var(--magenta), var(--blue) 30%, var(--teal) 45%, var(--green) 55%, var(--yellow) 70%, var(--orange) 85%, var(--red)); }

  .hero { position: absolute; top: 89px; left: 0; width: 1200px; height: 597px; }
  .hero-photo { position: absolute; inset: 0;
    background:
      radial-gradient(ellipse 420px 260px at 180px 330px, var(--glow-teal), transparent 70%),
      radial-gradient(ellipse 380px 220px at 650px 420px, var(--glow-amber), transparent 70%),
      radial-gradient(ellipse 500px 240px at 900px 160px, var(--shade-mid), transparent 75%),
      linear-gradient(180deg, var(--shade-mid), var(--shade-deep)); }

  .hero-copy { position: absolute; top: 160px; left: 0; width: 1227px; text-align: center; font-family: "Roboto Condensed", "Arial Narrow", sans-serif; font-weight: 700; text-transform: uppercase; }
  .hero-title { font-size: 44px; line-height: 54px; color: var(--gold); }
  .hero-text { font-size: 29.7px; line-height: 39px; color: var(--white); }

  .slide-arrow { position: absolute; top: 231px; width: 36px; height: 36px; border-radius: 50%; background: var(--arrow-bg); }
  .slide-arrow svg { display: block; }
  .slide-arrow.prev { left: 88px; }
  .slide-arrow.next { left: 1079px; }

  .ridge-art { position: absolute; left: 42px; bottom: 0; width: 1120px; height: 166px;
    background:
      linear-gradient(180deg, transparent 0%, rgba(0,0,0,0.55) 55%, var(--ink) 100%),
      linear-gradient(90deg, var(--magenta), var(--violet) 12%, var(--blue) 22%, var(--teal) 50%, var(--green) 62%, var(--lime) 68%, var(--yellow) 76%, var(--orange) 86%, var(--red) 94%, var(--magenta));
    opacity: 0.85; }
</style>
</head>
<body>
<div class="site">
  <header class="masthead">
    <div class="brand">VERMILION REEL WORKS</div>
    <nav class="main-nav">
      <a class="nav-home is-active" href="#">HOME</a>
      <a class="nav-about" href="#">ABOUT US</a>
      <a class="nav-team" href="#">TEAM</a>
      <a class="nav-services" href="#">SERVICES</a>
      <a class="nav-facility" href="#">FACILITY</a>
      <a class="nav-contact" href="#">CONTACT</a>
      <a class="nav-career" href="#">CAREER</a>
    </nav>
  </header>
  <div class="spectrum-rule"></div>

  <section class="hero">
    <div class="hero-photo" role="img" aria-label="Close-up photo of a lit audio mixing console with glowing knobs and buttons"></div>
    <div class="ridge-art" role="img" aria-label="Faceted rainbow-coloured mountain ridge graphic along the bottom of the banner"></div>
    <div class="hero-copy">
      <h1 class="hero-title">VERMILION REEL WORKS</h1>
      <p class="hero-text">Provides a&nbsp; well-designed working environment<br>which amplifies your team’s ability to reach their creative goals.</p>
    </div>
    <a class="slide-arrow prev" href="#" aria-label="Previous slide">
      <svg width="36" height="36" viewBox="0 0 36 36"><path d="M21 9 L13 18 L21 27" fill="none" stroke="#fff" stroke-width="1.6"/></svg>
    </a>
    <a class="slide-arrow next" href="#" aria-label="Next slide">
      <svg width="36" height="36" viewBox="0 0 36 36"><path d="M15 9 L23 18 L15 27" fill="none" stroke="#fff" stroke-width="1.6"/></svg>
    </a>
  </section>
</div>
</body>
</html>
```